Website design for an existing WordPress theme

Looking to get an experienced designer to help design a renewed informative website for a company in the field of digital sports media.

The website is already built using WordPress with a theme called "Quiver" from LayoutBazaar:
http://layoutbazaar.example/item/quiver-premium-multipurpose-wordpress-theme/3162084

We simply require to complete the graphic design, including:

* Taking our logo colors into consideration.
* Setting a Color Scheme.
* Typographical hierarchy - fonts and sizes (based on Google fonts)
* Background images
* Design for information boxes (if needed)

The website includes only 3-4 main pages:
1) Home page - including concept and product description - this requires the most design work.
2) Technology - short information page - needs some images.
3) About / Team - a short paragraph about the company and small biography paragraphs about each of the founders.
4) Contact us form

Check out the existing page here: http://www.fieldlenz.example/wordpress/

Redesign the existing informational website.
Notice the logo colors.

An example website:
http://www.quikreel.example/corp/
Maybe with sports pictures in the background, but we're not sure about it.

We also need the main image, on the top of the page - redesigned and adapted.
An image characterizing this main explanatory image is attached to this project description.

```html
<!DOCTYPE html>
<html lang="en">
<head>
<meta charset="utf-8">
<title>FieldLenz – Take The Lead</title>
<link rel="stylesheet" href="https://fonts.googleapis.com/css2?family=Open+Sans:wght@300;400;600&family=Oswald:wght@500;600&display=swap">
<style>
:root{
  --brand-orange:#f5a300;
  --label-orange:#f4a81c;
  --navy-deep:#070d1f;
  --navy-mid:#12306a;
  --button-blue:#0f2a78;
  --ink:#1a1a1a;
  --white:#ffffff;
  --title-bg:rgba(40,48,66,.82);
}
*{margin:0;padding:0;box-sizing:border-box}
html,body{width:1200px;height:635px;overflow:hidden;background:var(--navy-deep)}
.page{position:relative;width:1200px;height:635px;font-family:"Open Sans",Arial,sans-serif}

.site-header{position:absolute;left:0;top:0;width:1200px;height:95px;background:var(--brand-orange)}
.brand{position:absolute;left:56px;top:14px;height:66px;display:flex;align-items:center;gap:12px;color:var(--white)}
.brand-mark{width:22px;height:22px;border-radius:50%;background:var(--white)}
.brand-name{font-weight:300;font-size:31px;letter-spacing:.2px}
.brand-tagline{font-weight:300;font-size:31px;margin-left:6px}
.main-nav{position:absolute;right:68px;top:31px;display:flex;align-items:center}
.main-nav a{color:var(--ink);text-decoration:none;font-size:17px;padding:0 22px;line-height:34px}
.main-nav a.nav-contact{background:var(--button-blue);color:var(--white);border-radius:4px;padding:0 14px;margin-left:18px}

.hero{position:absolute;left:0;top:95px;width:1200px;height:540px;overflow:hidden}
.hero-backdrop{position:absolute;inset:0;
  background:
    radial-gradient(ellipse 60% 45% at 50% 22%, rgba(120,180,240,.55), transparent 70%),
    radial-gradient(ellipse 70% 30% at 50% 58%, rgba(40,110,170,.55), transparent 75%),
    linear-gradient(180deg,#0b1a3a 0%,var(--navy-mid) 35%,#0d2446 60%,var(--navy-deep) 78%,var(--navy-deep) 100%)}
.hero-title{position:absolute;left:228px;top:10px;width:730px;height:58px;background:var(--title-bg);color:var(--white);
  font-family:"Oswald",Arial,sans-serif;font-weight:500;font-size:33px;letter-spacing:1px;text-align:center;line-height:58px}

.flow-icon,.flow-arrow{position:absolute}
.flow-label{position:absolute;font-family:"Oswald",Arial,sans-serif;font-weight:600;color:var(--label-orange);
  font-size:21px;line-height:21px;text-align:center;text-transform:uppercase;letter-spacing:.3px}
.icon-placeholder{position:absolute;border-radius:8px}
.editing-art{left:366px;top:211px;width:129px;height:112px;background:linear-gradient(135deg,#3b4d7a,#7fa4d8 55%,#1d2a44)}
.distribution-art{left:919px;top:220px;width:189px;height:77px;background:linear-gradient(180deg,#f4f6fa,#c9d2e0)}

.hero-tagline{position:absolute;left:0;bottom:14px;width:1200px;text-align:center;color:var(--white);
  font-family:"Oswald",Arial,sans-serif;font-weight:500;font-size:22px;letter-spacing:.8px;text-transform:uppercase}
</style>
</head>
<body>
<div class="page">
  <header class="site-header">
    <div class="brand">
      <span class="brand-mark"></span>
      <span class="brand-name">FieldLenz</span>
      <span class="brand-tagline">Take The Lead</span>
    </div>
    <nav class="main-nav">
      <a href="#">Home</a>
      <a href="#">About</a>
      <a href="#" class="nav-contact">Contact Us</a>
    </nav>
  </header>

  <section class="hero">
    <div class="hero-backdrop" role="img" aria-label="Floodlit sports stadium at night with crowd and pitch"></div>
    <h1 class="hero-title">POWERING DIGITAL SPORTS VIDEO CONTENT</h1>

    <svg class="flow-icon" style="left:96px;top:205px" width="101" height="112" viewBox="0 0 101 112" aria-hidden="true">
      <g fill="#fff">
        <circle cx="22" cy="18" r="16"/>
        <circle cx="58" cy="18" r="16"/>
        <rect x="6" y="36" width="64" height="34" rx="4"/>
        <polygon points="70,44 96,32 96,74 70,62"/>
        <rect x="34" y="70" width="8" height="12"/>
        <polygon points="38,80 12,112 20,112 38,90 56,112 64,112"/>
        <rect x="35" y="80" width="6" height="32"/>
      </g>
    </svg>
    <div class="flow-label" style="left:60px;top:343px;width:160px">Live Sports</div>

    <svg class="flow-arrow" style="left:250px;top:232px" width="66" height="36" viewBox="0 0 66 36" aria-hidden="true">
      <g fill="#fff"><rect x="0" y="8" width="5" height="20"/><rect x="9" y="8" width="5" height="20"/><rect x="18" y="8" width="5" height="20"/><rect x="27" y="8" width="5" height="20"/><rect x="36" y="8" width="8" height="20"/><polygon points="44,0 66,18 44,36"/></g>
    </svg>

    <div class="icon-placeholder editing-art" role="img" aria-label="Film strip with magic wand illustration"></div>
    <div class="flow-label" style="left:320px;top:355px;width:220px">Automatic Real<br>Time Editing</div>

    <svg class="flow-arrow" style="left:544px;top:246px" width="66" height="36" viewBox="0 0 66 36" aria-hidden="true">
      <g fill="#fff"><rect x="0" y="8" width="5" height="20"/><rect x="9" y="8" width="5" height="20"/><rect x="18" y="8" width="5" height="20"/><rect x="27" y="8" width="5" height="20"/><rect x="36" y="8" width="8" height="20"/><polygon points="44,0 66,18 44,36"/></g>
    </svg>

    <svg class="flow-arrow" style="left:616px;top:170px" width="66" height="66" viewBox="0 0 66 36" aria-hidden="true" overflow="visible">
      <g fill="#fff" transform="translate(6,52) rotate(-45)"><rect x="0" y="8" width="5" height="20"/><rect x="9" y="8" width="5" height="20"/><rect x="18" y="8" width="5" height="20"/><rect x="27" y="8" width="5" height="20"/><rect x="36" y="8" width="8" height="20"/><polygon points="44,0 66,18 44,36"/></g>
    </svg>

    <svg class="flow-arrow" style="left:596px;top:284px" width="66" height="66" viewBox="0 0 66 36" aria-hidden="true" overflow="visible">
      <g fill="#fff" transform="translate(18,-14) rotate(45)"><rect x="0" y="8" width="5" height="20"/><rect x="9" y="8" width="5" height="20"/><rect x="18" y="8" width="5" height="20"/><rect x="27" y="8" width="5" height="20"/><rect x="36" y="8" width="8" height="20"/><polygon points="44,0 66,18 44,36"/></g>
    </svg>

    <svg class="flow-arrow" style="left:689px;top:246px" width="66" height="36" viewBox="0 0 66 36" aria-hidden="true">
      <g fill="#fff"><rect x="0" y="8" width="5" height="20"/><rect x="9" y="8" width="5" height="20"/><rect x="18" y="8" width="5" height="20"/><rect x="27" y="8" width="5" height="20"/><rect x="36" y="8" width="8" height="20"/><polygon points="44,0 66,18 44,36"/></g>
    </svg>

    <svg class="flow-arrow" style="left:820px;top:246px" width="66" height="36" viewBox="0 0 66 36" aria-hidden="true">
      <g fill="#fff"><rect x="0" y="8" width="5" height="20"/><rect x="9" y="8" width="5" height="20"/><rect x="18" y="8" width="5" height="20"/><rect x="27" y="8" width="5" height="20"/><rect x="36" y="8" width="8" height="20"/><polygon points="44,0 66,18 44,36"/></g>
    </svg>

    <svg class="flow-icon" style="left:694px;top:79px" width="148" height="135" viewBox="0 0 148 135" aria-hidden="true">
      <g fill="none" stroke="#fff" stroke-width="9">
        <rect x="14" y="5" width="84" height="56"/>
        <rect x="60" y="40" width="82" height="56"/>
        <rect x="5" y="72" width="84" height="50"/>
      </g>
      <g fill="#fff">
        <rect x="36" y="122" width="22" height="8"/><rect x="26" y="129" width="42" height="6"/>
        <rect x="112" y="96" width="8" height="14"/><rect x="100" y="108" width="32" height="6"/>
      </g>
    </svg>
    <div class="flow-label" style="left:863px;top:130px;width:200px;text-align:left">Fan Engagement</div>

    <svg class="flow-icon" style="left:684px;top:329px" width="94" height="84" viewBox="0 0 94 84" aria-hidden="true">
      <path d="M22 4h42l20 20v56H22z" fill="none" stroke="#fff" stroke-width="7" stroke-linejoin="round"/>
      <path d="M64 4v20h20" fill="none" stroke="#fff" stroke-width="6"/>
      <g fill="#fff"><rect x="44" y="40" width="30" height="5"/><rect x="44" y="52" width="30" height="5"/><rect x="44" y="64" width="30" height="5"/></g>
      <g transform="translate(2,76) rotate(-50)"><rect x="0" y="-6" width="60" height="12" fill="#fff"/><polygon points="0,-6 -10,0 0,6" fill="#fff"/></g>
    </svg>
    <div class="flow-label" style="left:640px;top:424px;width:200px">Automatic Real<br>Time Editing</div>

    <div class="icon-placeholder distribution-art" role="img" aria-label="Devices showing social network and video channel tiles"></div>
    <div class="flow-label" style="left:903px;top:318px;width:240px">Distribution to<br>Digital Landscape</div>

    <p class="hero-tagline">Maximize sports content value on digital with automagical video editing and publishing</p>
  </section>
</div>
</body>
</html>
```